New business card and stationary Project
Bright Meadow Orthodontics
New business card and stationary Project - Health
Creative Brief
Use same font as used in my logo
Bright & Fun-filled
Dr. Minh Tao
Orthodontist
3840 SE 167th Avenue, Suite #214 Camas, WA 98607
hello@brightmeadowgrins.example
BrightMeadowGrins.example
An existing Orthodontic Practice that move to a new location with a new name, and a new image. We are seeking a new design for business cards, letterhead, referral pads, envelopes, thank you cards, etc. We specialize in straightening teeth and improve facial profile and balance. The more creative the design the better. We are looking for something that is classy and high end yet some elements of fun in the design. *** I particular like the art of the curved lines used below the images (in the center of the web page) in our other practice : www.taoaligners.example (however, please use the gradient shades of colors of blue and orange to match our current logo of Bright Meadow Orthodontics). ***Our new practice will have sports theme decoration.
Watermark of the logo? any other information you think would fit. should my name, address, phones, web address, email address be place in the front or the back? I suppose it depends on the design.
pralko pralko
Designers, thank you for submitting your designs. I'm still looking for a unique, one of a kind design with a WOW. It can be simple yet has an edge of elegance and fun to it. I like asymmetrical look also. Please use the gradient in colors of orange and blue. Please add a subtle sport theme into the designs. thank you. Look forward to see your designs. Dr.Tao
Pluvorcraft, For your design #71, please help include the stationary so I can see the complete picture. Thank you. DR.Tao
Inkharborstudio, Thank you for your designs. Please help me include the stationary in for design #88 so I can see the complete package. Thank you. Dr.Tao
Pluvorcraft, thank you for submitting your designs. For the "star" rated design with the curved lines, please help me revise some of those designs to the curved lines similar to what's shown on my website for my other practice at: www.taoaligners.example (the curved lines below the changing pictures in the middle of the page,I like how those curved lines become transparent as they come out toward the edges), and please continue to use the gradient of colors too. thank you. DR.Tao
Dear designer Quillvantage7, Thank you for submitting your designs. For the designs I rated "star", please help include the stationary design so I can see the whole picture of everything. thank you. DR.Tao
Designers, Also please submit the designs for the presentation folders, thank you cards, etc. this will help me look at the overall picture of the stationary in order to me to give better inputs into your designs. thanks. Dr.tao
Designers, thank you for your creative designs of the business cards. Does designs of the letterhead and envelopes be posted after choosing the finalized designs of the business cards? It's hard for me to choose the design of the business cards without the designs of the letterhead and the envelopes along side. Dr.Tao
Designers, great designs thus far. we have just guaranteed the prize. please keep the creative designs coming in. some design ideas would be to incorporate the 'sports theme' into your designs. thanks!

```html
<!DOCTYPE html>
<html lang="en">
<head>
<meta charset="utf-8">
<title>Bright Meadow Orthodontics – Business Card</title>
<link href="https://fonts.googleapis.com/css2?family=Open+Sans:wght@400;600;700&display=swap" rel="stylesheet">
<style>
  :root {
    --backdrop: #e9e6e1;
    --card-white: #ffffff;
    --card-grey: #8d8f92;
    --ink: #2b2b2b;
    --ink-soft: #4a4a4a;
    --brand-blue: #1f5fa8;
    --brand-orange: #f07a1e;
    --brand-red: #e2392b;
    --accent-green: #7bb342;
  }
  * { box-sizing: border-box; margin: 0; padding: 0; }
  html, body { width: 1200px; height: 818px; overflow: hidden; }
  body {
    background: var(--backdrop);
    font-family: "Open Sans", Arial, sans-serif;
    position: relative;
  }
  .card {
    position: absolute;
    top: 254px;
    width: 540px;
    height: 309px;
    border-radius: 3px;
    box-shadow: 0 6px 18px rgba(0,0,0,0.18);
    overflow: hidden;
  }
  /* Back of card */
  .card-back { left: 40px; background: var(--card-grey); }
  .card-back .watermark-name {
    position: absolute;
    left: 250px; top: 120px;
    width: 260px;
    color: var(--card-white);
    font-weight: 600;
    font-size: 22px;
    line-height: 1.25;
    text-align: center;
    opacity: 0.95;
  }
  .card-back .vertical-url {
    position: absolute;
    left: 22px; bottom: 30px;
    transform-origin: left bottom;
    transform: rotate(-90deg) translate(0, 100%);
    color: var(--card-white);
    font-size: 13px;
    letter-spacing: 1.5px;
    white-space: nowrap;
  }
  /* Front of card */
  .card-front { left: 620px; background: var(--card-white); }
  .top-band {
    position: absolute; left: 0; top: 26px;
    width: 270px; height: 8px;
    background: linear-gradient(90deg, var(--brand-red), var(--brand-orange) 45%, rgba(240,122,30,0));
  }
  .bottom-band {
    position: absolute; right: 0; bottom: 22px;
    width: 230px; height: 8px;
    background: linear-gradient(90deg, rgba(31,95,168,0), var(--brand-blue));
  }
  .brand-name {
    position: absolute;
    left: 30px; top: 158px;
    width: 210px;
    color: var(--brand-blue);
    font-weight: 700;
    font-size: 23px;
    line-height: 1.2;
    text-align: center;
  }
  .sport-dots {
    position: absolute; left: 62px; top: 232px;
    display: flex; gap: 22px;
  }
  .sport-dots span { width: 9px; height: 9px; border-radius: 50%; }
  .contact-block {
    position: absolute; left: 296px; top: 44px;
    color: var(--ink);
  }
  .doctor-name { font-weight: 700; font-size: 14px; }
  .doctor-title { font-size: 12px; color: var(--ink-soft); margin-top: 1px; }
  .address { font-size: 12px; line-height: 1.35; margin-top: 24px; color: var(--ink-soft); }
  .contact-list { list-style: none; margin-top: 20px; }
  .contact-list li {
    display: flex; align-items: center; gap: 7px;
    font-size: 12.5px; line-height: 1; margin-bottom: 5px; color: var(--ink);
  }
  .contact-list svg { width: 14px; height: 14px; flex: none; }
</style>
</head>
<body>

<section class="card card-back" aria-label="Back of business card">
  <p class="watermark-name">Bright Meadow Orthodontics</p>
  <p class="vertical-url">BrightMeadowGrins.example</p>
</section>

<section class="card card-front" aria-label="Front of business card">
  <div class="top-band"></div>
  <div class="bottom-band"></div>

  <p class="brand-name">Bright Meadow Orthodontics</p>
  <div class="sport-dots" aria-hidden="true">
    <span style="background:var(--brand-orange)"></span>
    <span style="background:var(--accent-green)"></span>
    <span style="background:var(--brand-red)"></span>
    <span style="background:var(--brand-blue)"></span>
  </div>

  <div class="contact-block">
    <p class="doctor-name">Dr. Minh Tao</p>
    <p class="doctor-title">Orthodontist</p>
    <p class="address">3840 SE 167th Avenue,<br>Suite #214<br>Camas, WA 98607</p>
    <ul class="contact-list">
      <li>
        <svg viewBox="0 0 14 14" aria-hidden="true"><circle cx="7" cy="7" r="7" fill="var(--brand-red)"/><path d="M4.5 3.5c.5-.3 1-.2 1.2.3l.5 1.2c.1.4 0 .7-.3.9l-.4.3c.4.9 1 1.6 1.9 2l.3-.4c.2-.3.6-.4.9-.3l1.2.5c.5.2.6.7.3 1.2-.6.9-1.6 1-2.6.5C5.6 8.9 4.6 7.8 4 6.2c-.3-1-.2-2 .5-2.7z" fill="#fff"/></svg>
        360-555-0147
      </li>
      <li>
        <svg viewBox="0 0 14 14" aria-hidden="true"><circle cx="7" cy="7" r="7" fill="var(--brand-red)"/><rect x="3.5" y="5" width="7" height="4.5" rx="0.6" fill="#fff"/><rect x="4.5" y="3" width="5" height="2.3" fill="#fff"/></svg>
        360-555-0182
      </li>
      <li>
        <svg viewBox="0 0 14 14" aria-hidden="true"><circle cx="7" cy="7" r="7" fill="var(--brand-orange)"/><rect x="3.3" y="4.5" width="7.4" height="5" fill="#fff"/><path d="M3.3 4.5L7 7.4l3.7-2.9" stroke="var(--brand-orange)" stroke-width="0.8" fill="none"/></svg>
        hello@brightmeadowgrins.example
      </li>
      <li>
        <svg viewBox="0 0 14 14" aria-hidden="true"><circle cx="7" cy="7" r="7" fill="var(--brand-blue)"/><circle cx="7" cy="7" r="3.8" stroke="#fff" stroke-width="0.9" fill="none"/><ellipse cx="7" cy="7" rx="1.6" ry="3.8" stroke="#fff" stroke-width="0.8" fill="none"/><path d="M3.2 7h7.6" stroke="#fff" stroke-width="0.8"/></svg>
        BrightMeadowGrins.example
      </li>
    </ul>
  </div>
</section>

</body>
</html>
```